Gestatlung flyer (2 pages) format selectable, based accompanying templates (logo, text) Projektflyer "intercultural cooking class with asylum seekers' data Friday evenings 17. 03 / 24.03 / 31.03 / 07.04 / Time: 18:30 Location: KB Merlital St. Gallen Title: Intercultural cooking class with asylum seekers text: cooking course is run by asylum seekers. Cooking together, outlandish specialties, exciting conversations Registration: until 24h before the event costs: Expenses participation at its discretion Logos: Quarzo Linde, Stifung Velmora. The logos should be listed as the sender and do not dominate the flyer. --------- Just be creative, everything is permitted and desired. The goal is that we make as many people as possible aware of this flyer. The flyers are distributed and the target audience is young adults. Dr Flyer should be correspondingly Modern, Emotianal and sales driven (screaming). Strong Typo, clearly legible and the content clearly structured. The shape of the flyer is free! In total we leave you as much creative freedom as possible. I am looking forward to the many great suggestions and am very excited about the results.

Target Market(s)

Young adults

Font styles to use
Serif
Sans Serif
Script

Requirements
Must have
• Textunterstüzung by appropriate images. Friendly design, bright colors. Very easy to read, weighted Title entsrprechend.
Nice to have
• Emotional Cook image or illustration
Should not have
• No picture with white and dark-skinned people.

```html
<!DOCTYPE html>
<html lang="de">
<head>
<meta charset="utf-8">
<title>Interkultureller Kochkurs – Flyer</title>
<link rel="stylesheet" href="https://fonts.googleapis.com/css2?family=Antonio:wght@700&family=Arimo&family=Nunito:wght@400;600;700&family=Oswald:wght@400&display=swap">
<style>
  :root {
    --magenta: #f23cf0;
    --cyan: #3ef8f8;
    --dark: #363636;
    --ink: #1e1e1e;
    --paper: #ffffff;
    --stage: #d9d9d9;
    --strip: #e6e6e6;
  }
  * { margin: 0; padding: 0; box-sizing: border-box; }
  html, body { width: 1200px; height: 1200px; overflow: hidden; background: var(--stage); }
  .canvas { position: relative; width: 1200px; height: 1200px; }
  .flyer {
    position: absolute; left: 180px; top: 10px;
    width: 866px; height: 1216px;
    transform: scale(0.9704); transform-origin: 0 0;
    background: var(--paper); overflow: hidden;
    font-family: "Nunito", sans-serif; color: var(--ink);
  }
  .flyer__art { position: absolute; inset: 0; width: 866px; height: 1216px; }

  .event-info {
    position: absolute; left: 472px; top: 594px; width: 380px;
    text-align: center; font-family: "Oswald", "Arial Narrow", sans-serif; font-weight: 400;
    font-size: 28px; line-height: 43px; color: var(--paper); white-space: nowrap;
  }
  .event-info .accent-magenta { color: var(--magenta); }
  .event-info .accent-cyan { color: var(--cyan); }

  .headline { position: absolute; left: 38px; top: 692px; width: 370px; }
  .headline__top, .headline__bottom {
    display: block; font-family: "Antonio", "Arial Narrow", sans-serif; font-weight: 700;
    color: var(--magenta); text-transform: uppercase; white-space: nowrap;
  }
  .headline__top { font-size: 62px; line-height: 68px; letter-spacing: -2px; }
  .headline__main {
    display: block; font-family: "Arimo", sans-serif; font-size: 62px; line-height: 64px;
    color: var(--ink); white-space: nowrap;
  }
  .headline__bottom { font-size: 48px; line-height: 54px; }

  .details { position: absolute; left: 40px; top: 880px; width: 420px; font-size: 17px; line-height: 24px; }
  .details__label { color: var(--magenta); font-weight: 700; font-size: 21px; line-height: 28px; margin-top: 12px; }

  .senders {
    position: absolute; left: 44px; top: 1124px;
    display: flex; align-items: center; gap: 34px;
  }
  .sender-name { font-family: "Nunito", sans-serif; font-weight: 700; font-size: 38px; color: var(--ink); }
  .sender-partner { display: flex; align-items: center; gap: 10px; }
  .sender-partner__mark { width: 18px; height: 18px; background: var(--magenta); }
  .sender-partner__name { font-family: "Nunito", sans-serif; font-weight: 700; font-size: 22px; color: #8a8a8a; }
</style>
</head>
<body>
<div class="canvas">
  <div class="flyer">
    <svg class="flyer__art" viewBox="0 0 866 1216" xmlns="http://www.w3.org/2000/svg">
      <defs>
        <linearGradient id="kitchenTone" x1="0" y1="0" x2="1" y2="1">
          <stop offset="0" stop-color="#d8cfc4"/>
          <stop offset="0.5" stop-color="#b98a78"/>
          <stop offset="1" stop-color="#7c6f68"/>
        </linearGradient>
        <linearGradient id="playfulTone" x1="0" y1="0" x2="0" y2="1">
          <stop offset="0" stop-color="#ecebe8"/>
          <stop offset="1" stop-color="#8f8a86"/>
        </linearGradient>
        <linearGradient id="platingTone" x1="0" y1="0" x2="1" y2="1">
          <stop offset="0" stop-color="#c8503c"/>
          <stop offset="1" stop-color="#e9d6c9"/>
        </linearGradient>
      </defs>

      <rect class="hero-photo" x="0" y="0" width="866" height="660" fill="url(#kitchenTone)"
            role="img" aria-label="Foto: junge Leute kochen gemeinsam in einer Küche"/>

      <path class="panel-white" d="M0,590 Q430,690 866,460 L866,1216 L0,1216 Z" fill="var(--paper)"/>
      <path class="panel-dark" d="M360,600 Q610,800 810,1216 L866,1216 L866,460 Q620,585 360,600 Z" fill="var(--dark)"/>
      <path class="stripe-magenta" d="M360,602 Q570,820 722,1216 L810,1216 Q600,800 360,602 Z" fill="var(--magenta)"/>
      <path class="band-white" d="M0,540 Q430,630 866,430 L866,446 Q430,650 0,553 Z" fill="var(--paper)"/>
      <path class="band-cyan" d="M0,553 Q430,650 866,446 L866,468 Q430,700 0,600 Z" fill="var(--cyan)"/>
      <path class="strip-bottom" d="M0,1194 L714,1194 L722,1216 L0,1216 Z" fill="var(--strip)"/>

      <ellipse cx="202" cy="660" rx="120" ry="10" fill="#000" opacity="0.12"/>
      <circle cx="202" cy="501" r="154" fill="var(--magenta)"/>
      <circle cx="202" cy="501" r="142" fill="var(--paper)"/>
      <circle class="photo-circle" cx="202" cy="501" r="136" fill="url(#playfulTone)"
              role="img" aria-label="Foto: zwei Personen posieren verspielt mit Gemüse"/>

      <circle cx="635" cy="963" r="154" fill="var(--cyan)"/>
      <circle cx="635" cy="963" r="142" fill="var(--paper)"/>
      <circle class="photo-circle" cx="635" cy="963" r="136" fill="url(#platingTone)"
              role="img" aria-label="Foto: eine Köchin richtet einen Teller an"/>
    </svg>

    <div class="event-info">
      <p>Daten: <span class="accent-magenta">Freitag Abende</span></p>
      <p class="accent-cyan">17. 03 / 24.03 - 31.03 / 07.04</p>
      <p>Zeit: <span class="accent-magenta">18.30h</span></p>
      <p>Ort: <span class="accent-cyan">KB Merlital St.Gallen</span></p>
    </div>

    <h1 class="headline">
      <span class="headline__top">Interkultureller</span>
      <span class="headline__main">KOCHKURS</span>
      <span class="headline__bottom">mit Asylsuchenden</span>
    </h1>

    <div class="details">
      <p>Kochkurs wird von Asylsuchenden geleitet.<br>Gemeinsames Kochen, fremdländische<br>Spezialiäten, spannende Gespräche</p>
      <p class="details__label">Anmeldung:</p>
      <p>bis 24h vor dem Anlass</p>
      <p class="details__label">Kosten:</p>
      <p>Unkostenbeteiligung nach eigenem Ermessen</p>
    </div>

    <div class="senders">
      <span class="sender-name">Quarzo Linde</span>
      <span class="sender-partner">
        <span class="sender-partner__mark"></span>
        <span class="sender-partner__name">Stifung Velmora</span>
      </span>
    </div>
  </div>
</div>
</body>
</html>
```